Redesign of Business Cards to Update them!

We want a full overhaul of our business cards! We have a design that is almost 5 years old and it needs to be updated to be current

Address is 437 Dunmore Lane Suite C San Bernardino CA 92408
PH: 9094718263
Zorlivo.com

Hours M-F 10AM-4PM
Sat and Sunday Closed

```html
<!DOCTYPE html>
<html lang="en">
<head>
<meta charset="utf-8">
<title>Zorlivo Business Card</title>
<link rel="stylesheet" href="https://fonts.googleapis.com/css2?family=Arimo:wght@400;700&display=swap">
<style>
  :root {
    --ink: #000000;
    --paper: #ffffff;
    --accent: #e8171c;
  }
  html, body {
    margin: 0;
    padding: 0;
    overflow: hidden;
    background: var(--paper);
  }
  .card {
    position: relative;
    width: 1200px;
    height: 704px;
    overflow: hidden;
    background: var(--ink);
    font-family: "Arimo", Arial, sans-serif;
    color: var(--paper);
  }
  .card-shapes {
    position: absolute;
    inset: 0;
  }
  .brand {
    position: absolute;
    left: 40px;
    width: 580px;
    top: 360px;
    display: flex;
    align-items: center;
    justify-content: center;
    gap: 20px;
    color: var(--ink);
  }
  .brand-dot {
    width: 44px;
    height: 44px;
    border-radius: 50%;
    background: var(--accent);
  }
  .brand-name {
    font-size: 76px;
    font-weight: 700;
    letter-spacing: 2px;
    line-height: 1;
  }
  .web-pill {
    position: absolute;
    left: 732px;
    top: 77px;
    width: 371px;
    height: 62px;
    border-radius: 31px;
    background: var(--paper);
    color: var(--ink);
    display: flex;
    align-items: center;
    justify-content: center;
    font-size: 31px;
    letter-spacing: 1px;
  }
  .address {
    position: absolute;
    left: 728px;
    top: 270px;
    margin: 0;
    font-style: normal;
    font-size: 31px;
    line-height: 38px;
  }
  .contact-row {
    position: absolute;
    left: 673px;
    display: flex;
    align-items: flex-start;
    gap: 20px;
  }
  .contact-row svg {
    width: 34px;
    height: 34px;
    flex: none;
  }
  .phone { top: 451px; font-size: 31px; }
  .hours { top: 528px; }
  .hours-main { font-size: 31px; line-height: 38px; display: block; }
  .hours-note { font-size: 27px; line-height: 34px; display: block; }
</style>
</head>
<body>
  <div class="card">
    <svg class="card-shapes" width="1200" height="704" viewBox="0 0 1200 704" aria-hidden="true">
      <polygon points="0,0 452,0 651,353 452,704 0,704" fill="var(--paper)"/>
      <polygon points="452,0 485,0 684,353 485,704 452,704 651,353" fill="var(--accent)"/>
      <polygon points="640,310 688,353 640,396 660,353" fill="var(--paper)"/>
    </svg>

    <div class="brand">
      <span class="brand-dot"></span>
      <span class="brand-name">Zorlivo</span>
    </div>

    <div class="web-pill">Zorlivo.com</div>

    <address class="address">437 Dunmore Lane Suite<br>C San Bernardino<br>CA 92408</address>

    <div class="contact-row phone">
      <svg viewBox="0 0 24 24" aria-hidden="true">
        <path d="M6.6 2.5 9.4 6c.4.5.4 1.2 0 1.7L8 9.3c1.2 2.6 3.6 5 6.3 6.3l1.6-1.4c.5-.4 1.2-.4 1.7 0l3.5 2.8c.5.4.6 1.1.2 1.6l-1.6 2.1c-.5.6-1.3.9-2 .7C10.6 19.6 4.5 13.5 2.6 6.4c-.2-.7.1-1.5.7-2L5 2.3c.5-.4 1.2-.3 1.6.2Z" fill="none" stroke="var(--accent)" stroke-width="1.8" stroke-linejoin="round"/>
        <path d="M14 3.5a7 7 0 0 1 6.5 6.5M14 7a3.5 3.5 0 0 1 3 3" fill="none" stroke="var(--accent)" stroke-width="1.8" stroke-linecap="round"/>
      </svg>
      <span>9094718263</span>
    </div>

    <div class="contact-row hours">
      <svg viewBox="0 0 24 24" aria-hidden="true">
        <circle cx="12" cy="12" r="9.5" fill="none" stroke="var(--accent)" stroke-width="2"/>
        <path d="M12 6.5V12l4 3" fill="none" stroke="var(--accent)" stroke-width="2" stroke-linecap="round"/>
      </svg>
      <div>
        <span class="hours-main">M-F 10AM-4PM</span>
        <span class="hours-note">Sat and Sunday Closed</span>
      </div>
    </div>
  </div>
</body>
</html>
```